Hearing Aid Company Website

Winner will be our future designer for our other brands. We need the website download to put into our Shopify account. We need a Shopify website done for a Hearing Aid Company called "Sonvel". We really need a creative modern site that has all the following pages that are also functional, not just empty pages. You can find stock photos and more online and information on hearing aids to add to the site. I will pay extra afterwards to really make the site exactly how I need after winner is picked. I've attached the necessary two products and also the pages I need on the site. I've also attached the logo. Make a really unique good looking site, feel free to add any pages or change anything you'd like you'd think would be best.
Top Page:
Hearing Aids (Products Attached)
Contact Us
Register your product (1 Year Warrenty)
Support
Track Order
Reviews
FAQ's
Careers
Bottom of Page:
Refund Policy
Privacy Policy
Terms of Conditions
Refund
Examples of websites I like:
https://quimbrelisten.com/
https://www.tovarlisteningaid.com/
https://www.plusaro.com/
https://www.vintu.com/
https://www.kolpe.com/
https://www.donmevo.com/

```html
<!DOCTYPE html>
<html lang="en">
<head>
<meta charset="utf-8">
<title>Sonvel — Hearing Aids</title>
<link href="https://fonts.googleapis.com/css2?family=Space+Grotesk:wght@400;500;600;700&family=Poppins:wght@400;500;600&display=swap" rel="stylesheet">
<style>
:root{
  --blue:#12a8ec;
  --blue-dark:#0a8fd0;
  --navy:#0b3a66;
  --ink:#111418;
  --muted:#5d636b;
  --line:#e3e7ec;
  --mint:#eafbef;
  --cream:#fff6df;
  --lilac:#eeeefc;
  --sky:#e8f4fd;
  --sun:#fdf8d6;
  --black:#050505;
  --white:#ffffff;
}
*{box-sizing:border-box;margin:0;padding:0}
html,body{width:1200px;height:3846px;overflow:hidden;background:var(--white)}
body{font-family:"Poppins",sans-serif;color:var(--ink);position:relative}
.head{font-family:"Space Grotesk",sans-serif}
.abs{position:absolute}
.btn{position:absolute;display:flex;align-items:center;justify-content:center;border-radius:16px;font-size:10px;font-weight:600;color:var(--white);background:var(--blue)}
.btn-navy{background:var(--navy);box-shadow:0 3px 0 #14b0f0}
.btn-outline{background:var(--white);color:var(--ink);border:1.5px solid var(--blue)}

/* top bar */
.promo{left:0;top:0;width:1200px;height:23px;background:var(--blue);color:var(--white);font-size:9px;display:flex;align-items:center}
.promo .msg{position:absolute;left:200px}
.promo .tel{position:absolute;left:818px;font-weight:600;font-size:10px}

/* header */
.header{left:0;top:23px;width:1200px;height:58px;border-bottom:1px solid var(--line)}
.brand{font-family:"Space Grotesk",sans-serif;font-weight:700;color:var(--ink);display:flex;align-items:center;gap:6px}
.brand .dot{width:10px;height:10px;border-radius:50%;background:var(--blue)}
.search{left:501px;top:15px;width:215px;height:26px;border-radius:13px;background:#f2f4f6;font-size:9px;color:var(--muted);padding-left:14px;display:flex;align-items:center}
.search .go{position:absolute;right:4px;top:4px;width:18px;height:18px;border-radius:50%;background:var(--blue)}
.hicon{top:12px;font-size:8px;color:var(--muted);text-align:center;width:50px}
.cart{left:907px;top:17px;width:93px;height:24px;border:1px solid #cfd5db;border-radius:12px;font-size:9px;display:flex;align-items:center;justify-content:center;gap:6px}

/* nav */
.nav{left:0;top:81px;width:1200px;height:38px;font-size:9px;font-weight:500}
.nav span{position:absolute;top:13px}
.nav .home{left:205px;top:8px;width:62px;height:22px;background:var(--blue);color:var(--white);display:flex;align-items:center;justify-content:center;clip-path:polygon(12% 0,100% 0,88% 100%,0 100%)}

/* hero */
.hero{left:0;top:119px;width:1200px;height:411px;background:linear-gradient(160deg,#ecf6fd 0%,#f6f8fb 55%,#fdf1e4 100%);overflow:hidden}
.hero h1{position:absolute;left:107px;top:88px;font-size:40px;line-height:48px;font-weight:700}
.hero p{position:absolute;left:107px;top:208px;width:370px;font-size:9.5px;line-height:16px;color:#333}
.pill{position:absolute;height:40px;border-radius:20px;background:var(--sun);border:2px solid var(--blue);font-size:11px;font-weight:600;display:flex;align-items:center;padding-left:48px}
.pill i{position:absolute;left:6px;top:6px;width:24px;height:24px;border-radius:50%;background:#1a2433}
.product-hero{left:740px;top:60px;width:330px;height:300px;border-radius:50%;background:radial-gradient(circle at 50% 45%,#5a5d63 0%,#2a2c30 45%,rgba(240,240,240,0) 70%)}

/* section titles */
.title{position:absolute;left:0;width:1200px;text-align:center;font-family:"Space Grotesk",sans-serif;font-weight:500;font-size:33px;line-height:40px}

/* photo grid */
.tile{position:absolute;border-radius:6px;overflow:hidden}
.tile span{position:absolute;font-family:"Space Grotesk",sans-serif;font-weight:600;font-size:21px;line-height:25px;color:var(--ink)}

/* info panel */
.info{left:107px;top:1613px;width:987px;height:462px;background:var(--mint);border-radius:8px}
.col{position:absolute;top:150px;width:240px;text-align:center}
.col + .col{border-left:1px solid #cfe8d6}
.col svg{display:block;margin:0 auto}
.col h3{font-size:11px;font-weight:600;margin-top:10px}
.col p{font-size:8.5px;line-height:13px;color:#444;margin:10px auto 0;width:170px}

/* reviews */
.review{position:absolute;top:2249px;width:248px;height:122px;border-radius:3px;padding:16px 18px;font-size:8.5px;line-height:17px;color:#333}
.review .stars{color:#e5532a;font-size:10px;letter-spacing:2px;margin-bottom:6px}
.author{position:absolute;top:2393px;display:flex;gap:10px;align-items:center;font-size:9.5px;font-weight:600}
.author i{width:34px;height:34px;border-radius:50%;background:linear-gradient(135deg,#e7c6a8,#8b6a52)}
.author small{display:block;font-weight:400;color:var(--muted);font-size:8px}
.arrow{position:absolute;top:2298px;font-size:18px;color:#555}

/* newsletter */
.news{left:0;top:2564px;width:1200px;height:322px;background:var(--sun);overflow:hidden}
.news h2{position:absolute;left:199px;top:70px;font-size:40px;font-weight:700}
.news p{position:absolute;left:199px;top:128px;font-size:9px;color:#333}
.news .email{position:absolute;left:199px;top:164px;width:410px;height:32px;border-radius:16px;background:var(--white);font-size:9px;padding-left:16px;display:flex;align-items:center}

/* faq */
.faq{position:absolute;left:259px;width:686px;font-size:10.5px;font-weight:600;border-bottom:1px solid var(--line);height:44px;padding-left:62px;display:flex;align-items:center}
.faq b{position:absolute;left:14px;color:var(--blue);font-size:18px;font-weight:400}

/* call band + footer */
.call{left:0;top:3446px;width:1200px;height:85px;background:var(--blue);color:var(--white);display:flex;align-items:center;justify-content:center;gap:12px;font-family:"Space Grotesk",sans-serif;font-size:24px}
.call strong{font-weight:700;font-size:26px}
.footer{left:0;top:3531px;width:1200px;height:315px;background:var(--black);color:var(--white)}
.fcol{position:absolute;top:48px;font-size:9px;line-height:22px}
.fcol h4{color:var(--blue);font-size:11px;font-weight:600;display:flex;align-items:center;gap:10px;margin-bottom:8px}
.fcol h4::after{content:"";width:100px;height:1px;background:var(--blue)}
.social{position:absolute;top:104px;width:26px;height:26px;border-radius:50%;background:#333}
</style>
</head>
<body>

<div class="abs promo"><span class="msg">Our Labor Day Sale is on! Save up to $99 off Sonvel devices. <b>Shop Now!</b></span><span class="tel">&#9743; 123-456-7890</span></div>

<header class="abs header">
  <div class="abs brand" style="left:199px;top:12px;font-size:26px">Sonvel<span class="dot"></span></div>
  <div class="abs search">Search products...<span class="go"></span></div>
  <div class="abs hicon" style="left:752px"><svg width="14" height="14" viewBox="0 0 14 14"><circle cx="7" cy="4.5" r="3" fill="none" stroke="#12a8ec" stroke-width="1.3"/><path d="M1.5 13c1-3.5 10-3.5 11 0" fill="none" stroke="#12a8ec" stroke-width="1.3"/></svg><br>Account</div>
  <div class="abs hicon" style="left:831px"><svg width="14" height="14" viewBox="0 0 14 14"><path d="M7 12.5 1.8 7.2a3 3 0 0 1 5.2-3.4 3 3 0 0 1 5.2 3.4Z" fill="none" stroke="#12a8ec" stroke-width="1.3"/></svg><br>Wish list</div>
  <div class="abs cart"><svg width="10" height="11" viewBox="0 0 10 11"><rect x="1" y="3" width="8" height="7" fill="none" stroke="#111" stroke-width="1.2"/><path d="M3 3a2 2 0 0 1 4 0" fill="none" stroke="#111" stroke-width="1.2"/></svg>$ 0.00</div>
</header>

<nav class="abs nav">
  <span class="home">Home</span>
  <span style="left:296px">Hearing Aids</span>
  <span style="left:390px">Register Your Product</span>
  <span style="left:551px">Support</span>
  <span style="left:637px">Track Order</span>
  <span style="left:722px">Reviews</span>
  <span style="left:796px">FAQ's</span>
  <span style="left:866px">Careers</span>
  <span style="left:949px">Contact Us</span>
</nav>

<section class="abs hero">
  <svg class="abs" style="left:0;top:0" width="1200" height="411"><path d="M760 0C600 120 600 330 790 411" fill="none" stroke="#9fd8f5" stroke-width="1.5"/><path d="M900 0c120 60 160 200 90 411" fill="none" stroke="#e3f2fb" stroke-width="24"/></svg>
  <h1 class="head">Hearing is<br>life-changing</h1>
  <p>Lorem Ipsum is simply dummy text of the printing and typesetting industry lorem Ipsum has been the industry's standard dummy established fact that a reader.</p>
  <div class="btn" style="left:107px;top:286px;width:163px;height:32px">Discover Hearing Aids</div>
  <div class="pill" style="left:589px;top:90px;width:243px"><i></i>Crystal Clear Sound</div>
  <div class="pill" style="left:525px;top:184px;width:245px"><i></i>Invisible to the Eye</div>
  <div class="pill" style="left:589px;top:280px;width:243px"><i></i>24h Battery Life</div>
  <div class="abs product-hero" role="img" aria-label="Black hearing aid charging case with two earbuds and small beige hearing aids"></div>
</section>

<h2 class="title" style="top:600px">Say goodbye to<br>traditional hearing aids</h2>

<div class="tile" style="left:107px;top:709px;width:593px;height:373px;background:linear-gradient(135deg,#c9d6c4,#8c9d86 60%,#6d7b88)" role="img" aria-label="Smiling senior couple holding coffee mugs at home"><span style="left:38px;top:40px">Engage with<br>Hearing Device</span></div>
<div class="tile" style="left:726px;top:709px;width:368px;height:373px;background:linear-gradient(160deg,#bfe6df,#8fd0c6)" role="img" aria-label="Young man in profile wearing an earbud style hearing aid, with charging case"><span style="left:30px;top:206px">New<br>Superior<br>Technology<br>for Everyone</span></div>
<div class="tile" style="left:107px;top:1107px;width:368px;height:371px;background:linear-gradient(160deg,#f6e8d2,#e4c4a0)" role="img" aria-label="Smiling man touching his ear-worn hearing aid"><span style="right:36px;top:30px;text-align:right">Design for<br>Ease</span></div>
<div class="tile" style="left:501px;top:1107px;width:593px;height:371px;background:linear-gradient(135deg,#d7dde3,#a9b3bd 55%,#e9ece9)" role="img" aria-label="Senior couple chatting in a bright kitchen"><span style="right:36px;top:30px;text-align:right">Our promise of<br>value</span></div>

<div class="btn btn-navy" style="left:514px;top:1514px;width:172px;height:28px">Shop Now Hearing Aids</div>

<section class="abs info">
  <h2 class="title" style="top:70px;width:987px;font-size:32px">Looking for more information?</h2>
  <div class="col" style="left:10px">
    <svg width="30" height="34" viewBox="0 0 30 34"><path d="M5 11h20l-2 20H7Z" fill="none" stroke="#222" stroke-width="1.6"/><path d="M10 11a5 5 0 0 1 10 0" fill="none" stroke="#222" stroke-width="1.6"/></svg>
    <h3>Shop products</h3><p>Lorem Ipsum is simply dummy text printing and industry.</p>
    <div class="btn btn-outline" style="left:58px;top:132px;width:124px;height:34px">Shop Now!</div>
  </div>
  <div class="col" style="left:250px">
    <svg width="30" height="34" viewBox="0 0 30 34"><rect x="8" y="2" width="15" height="30" rx="3" fill="none" stroke="#222" stroke-width="1.6"/><circle cx="15.5" cy="17" r="4" fill="none" stroke="#12a8ec" stroke-width="1.6"/></svg>
    <h3>Video guides</h3><p>Lorem Ipsum is simply dummy text printing and industry.</p>
    <div class="btn btn-outline" style="left:58px;top:132px;width:124px;height:34px">Video Guides</div>
  </div>
  <div class="col" style="left:490px">
    <svg width="34" height="34" viewBox="0 0 34 34"><rect x="3" y="10" width="28" height="20" rx="2" fill="none" stroke="#222" stroke-width="1.6"/><path d="M7 10 22 3l4 7" fill="none" stroke="#222" stroke-width="1.6"/><rect x="22" y="17" width="9" height="6" fill="none" stroke="#12a8ec" stroke-width="1.6"/></svg>
    <h3>Financing</h3><p>Lorem Ipsum is simply dummy text printing and industry.</p>
    <div class="btn btn-outline" style="left:58px;top:132px;width:124px;height:34px">Financing info</div>
  </div>
  <div class="col" style="left:730px">
    <svg width="34" height="34" viewBox="0 0 34 34"><circle cx="17" cy="12" r="7" fill="none" stroke="#222" stroke-width="1.6"/><path d="M5 32c2-9 22-9 24 0" fill="none" stroke="#222" stroke-width="1.6"/><path d="M9 12a8 8 0 0 1 16 0" fill="none" stroke="#12a8ec" stroke-width="1.6"/></svg>
    <h3>Still need help?</h3><p>Lorem Ipsum is simply dummy text printing and industry.</p>
    <div class="btn btn-outline" style="left:58px;top:132px;width:124px;height:34px">&#9743;&nbsp;123-456-7890</div>
  </div>
</section>

<h2 class="title" style="top:2141px">Making a difference in the<br>lives of 1000+ people</h2>
<span class="arrow" style="left:147px">&#8249;</span>
<span class="arrow" style="left:1043px">&#8250;</span>
<div class="review" style="left:201px;background:var(--cream)"><div class="stars">★★★★★</div>"There are many variations of passages lorem Ipsum available, but the majority have suffered alteration in some form, by injected humour, or randomised..."</div>
<div class="review" style="left:478px;background:var(--lilac)"><div class="stars">★★★★★</div>"There are many variations of passages lorem Ipsum available, but the majority have suffered alteration in some form, by injected humour, or randomised..."</div>
<div class="review" style="left:752px;background:var(--sky)"><div class="stars">★★★★★</div>"There are many variations of passages lorem Ipsum available, but the majority have suffered alteration in some form, by injected humour, or randomised..."</div>
<div class="author" style="left:228px"><i role="img" aria-label="Reviewer portrait"></i><div>Standard Chunk<small>Lorem industry</small></div></div>
<div class="author" style="left:504px"><i role="img" aria-label="Reviewer portrait"></i><div>Finibus Bonorum<small>Lorem industry</small></div></div>
<div class="author" style="left:780px"><i role="img" aria-label="Reviewer portrait"></i><div>J. Pellworth<small>Lorem industry</small></div></div>
<div class="btn btn-navy" style="left:514px;top:2475px;width:172px;height:28px">View All Reviews</div>

<section class="abs news">
  <svg class="abs" style="left:0;top:0" width="1200" height="322"><path d="M880 0C860 60 900 160 960 322" fill="none" stroke="#7dcfa8" stroke-width="1"/><ellipse cx="1060" cy="140" rx="150" ry="170" fill="#eef9ee"/></svg>
  <h2 class="head">Stay in touch</h2>
  <p>Joining our mailing list, and receive some of the best deals possible..</p>
  <div class="email">Enter your email...</div>
  <div class="btn" style="left:199px;top:210px;width:94px;height:30px">Subscribe</div>
  <div class="abs" style="left:836px;top:50px;width:300px;height:230px;border-radius:50%;background:radial-gradient(circle at 55% 50%,#2b2d31 0%,#111 40%,rgba(238,249,238,0) 68%)" role="img" aria-label="Black hearing aid case with earbuds and charging cable"></div>
</section>

<h2 class="title" style="top:2955px;font-size:31px">Frequently asked questions</h2>
<div class="faq" style="top:3024px"><b>+</b>Contrary to popular belief, lorem Ipsum?</div>
<div class="abs" style="left:259px;top:3068px;width:686px;height:124px;background:linear-gradient(90deg,#fdf3e7,#eef4fc)">
  <div class="abs" style="left:14px;top:18px;width:12px;height:2px;background:#222"></div>
  <div class="abs" style="left:62px;top:12px;font-size:10.5px;font-weight:600">It is a long established fact that a reader will be distracted?</div>
  <div class="abs" style="left:62px;top:44px;width:580px;font-size:9.5px;line-height:18px;color:#333">Lorem ipsum dolor sit amet, consectetur adipiscing elit, sed do eiusmod tempor incididunt ut labore et dolore magna aliqua. Ut enim ad minim veniam, quis nostrud exercitation ullamco laboris nisi ut aliquip ex ea commodo consequat.</div>
</div>
<div class="faq" style="top:3184px"><b>+</b>There are many variations of passages of lorem Ipsum?</div>
<div class="faq" style="top:3231px"><b>+</b>Contrary to popular belief, lorem Ipsum?</div>
<div class="faq" style="top:3280px"><b>+</b>There are many variations of passages of lorem Ipsum?</div>
<div class="faq" style="top:3327px;border-bottom:none"><b>+</b>Contrary to popular belief, lorem Ipsum?</div>

<div class="abs call">Have questions? Call us now! <strong>123-456-7890</strong></div>

<footer class="abs footer">
  <div class="abs brand" style="left:104px;top:60px;font-size:44px;color:var(--white)">Sonvel<span class="dot" style="width:14px;height:14px"></span></div>
  <span class="social" style="left:136px"></span>
  <span class="social" style="left:174px;background:var(--blue)"></span>
  <span class="social" style="left:212px"></span>
  <div class="fcol" style="left:382px"><h4>Contact us</h4>
    <div><span style="color:var(--blue)">&#9743;</span>&nbsp; 123-456-7890</div>
    <div><span style="color:var(--blue)">&#9993;</span>&nbsp; info@sonvel.com</div>
    <div style="line-height:16px;margin-top:4px"><span style="color:var(--blue)">&#9679;</span>&nbsp; <span style="color:var(--blue)">Sonvel</span><br>&nbsp;&nbsp;&nbsp;&nbsp;Lorem ipsum Str., Neo dammy, 142<br>&nbsp;&nbsp;&nbsp;&nbsp;design - MH, 1234</div>
  </div>
  <div class="fcol" style="left:649px"><h4>Quick links</h4>Home<br>Hearing Aids<br>Register Your Product<br>Support<br>Track Order</div>
  <div class="fcol" style="left:786px;top:78px">Reviews<br>FAQ's<br>Careers<br>Contact Us</div>
  <div class="fcol" style="left:917px"><h4>Policies</h4>Refund Policy<br>Privacy Policy<br>Terms of Conditions</div>
  <div class="abs" style="left:104px;top:264px;width:992px;height:1px;background:#333"></div>
  <svg class="abs" style="left:1070px;top:240px" width="14" height="14" viewBox="0 0 14 14"><path d="M7 1 13 13 7 9 1 13Z" fill="#12a8ec"/></svg>
  <div class="abs" style="left:0;top:283px;width:1200px;text-align:center;font-size:8.5px">© 2024 <span style="color:var(--blue)">Sonvel</span>. All Rights Reserved.</div>
</footer>

</body>
</html>
```